silverbrook gymnastics academy

need a website for above to contain information about the academy, enrollment form etc..

Need a web design for new business Silverbrook Gymnastics Academy offering classes in gymnastics. Info on the business is in the doc called "Web design" which details the tabs I will need on my page. Please see our Facebook page to get an idea of the style Silverbrookgymnasticsacademy.

Thank you for your help. I do not require hosting of a domain name just need it all ready to be hosted. Thanks

Budget now increased to include the coding of the website as well.

```html
<!DOCTYPE html>
<html lang="en">
<head>
<meta charset="utf-8">
<title>Silverbrook Gymnastics Academy</title>
<link rel="stylesheet" href="https://fonts.googleapis.com/css2?family=Montserrat:wght@300;400;600;700;800&family=Lato:wght@400;700&family=Kalam&display=swap">
<style>
:root{
  --yellow:#f2cc1c;
  --yellow-deep:#e4ab00;
  --black:#000;
  --white:#fff;
  --ink:#1d1d1d;
  --grey-text:#555;
  --search-bg:#f1f1f1;
}
*{box-sizing:border-box;margin:0;padding:0}
html,body{width:704px;height:1200px;overflow:hidden;background:var(--white)}
body{position:relative;font-family:'Lato',sans-serif;color:var(--ink)}
.abs{position:absolute}

.site-header{left:0;top:0;width:704px;height:322px;background:radial-gradient(ellipse at 50% 30%,#f6dc3a 0%,var(--yellow) 40%,var(--yellow-deep) 100%)}
.brand{left:0;top:36px;width:704px;text-align:center;font-family:'Montserrat',sans-serif;font-weight:700;font-size:15px;letter-spacing:.5px;color:var(--ink)}
.tagline{left:0;width:704px;top:85px;text-align:center;font-family:'Kalam',cursive;font-size:12px;color:var(--black)}
.hero{left:101px;top:110px;width:502px;height:190px;background:linear-gradient(135deg,#5a3426 0%,#8a5a48 40%,#3d2219 100%);box-shadow:0 14px 14px -8px rgba(80,60,0,.55)}
.hero-title{left:0;top:8px;width:502px;text-align:center;font-family:'Montserrat',sans-serif;font-weight:300;font-size:29px;color:var(--white)}
.hero-dots{left:13px;top:170px;display:flex;gap:5px}
.hero-dots span{width:6px;height:6px;border-radius:50%;background:var(--white)}
.hero-dots span:first-child{background:var(--yellow)}

.main-nav{left:0;top:322px;width:704px;height:49px;background:var(--black)}
.main-nav a{position:absolute;top:0;line-height:49px;font-family:'Montserrat',sans-serif;font-weight:700;font-size:9.6px;color:var(--white);text-decoration:none}
.search{left:463px;top:19px;width:130px;height:17px;background:var(--search-bg);border-radius:3px;font-size:7px;font-style:italic;color:#444;padding:4px 0 0 7px}
.search svg{position:absolute;right:8px;top:4px}

.welcome-title{left:0;width:704px;top:391px;text-align:center;font-family:'Montserrat',sans-serif;font-weight:700;font-size:16px;color:var(--ink)}
.welcome-text{left:114px;width:476px;top:421px;text-align:center;font-size:9.4px;line-height:12px;color:var(--grey-text)}

.about{left:101px;top:476px;width:502px;height:171px;background:linear-gradient(180deg,#0b1624 0%,#14253a 55%,#2d2a28 80%,#121212 100%);color:var(--white);text-align:center}
.about h2{position:absolute;left:0;width:502px;top:48px;font-family:'Montserrat',sans-serif;font-weight:700;font-size:15px}
.about p{position:absolute;left:40px;width:422px;top:85px;font-size:9.4px;line-height:15px}

.aims{left:0;top:686px;width:704px;height:218px;background:radial-gradient(ellipse at 50% 20%,#f6dc3a 0%,var(--yellow) 45%,var(--yellow-deep) 100%)}
.aims h2{position:absolute;left:0;width:704px;top:16px;text-align:center;font-family:'Montserrat',sans-serif;font-weight:800;font-size:15px;color:var(--black)}
.aim-card{position:absolute;top:48px;width:154px;height:138px;background:var(--black)}
.aim-photo{height:98px}
.aim-card p{position:absolute;left:7px;top:108px;width:144px;padding-left:10px;font-family:'Lato',sans-serif;font-weight:700;font-size:7.2px;line-height:9px;color:var(--white)}
.aim-card p::before{content:"›";position:absolute;left:0;top:-2px;font-size:10px}

.media{left:0;top:904px;width:704px;height:249px;background:var(--black);color:var(--white)}
.media h3{position:absolute;top:24px;font-family:'Montserrat',sans-serif;font-weight:700}
.videos-title{left:100px;font-size:12px}
.ads-title{left:421px;font-size:9px;top:27px!important}
.video-arrows{left:383px;top:26px}
.video-frame{left:101px;top:49px;width:303px;height:174px;border:4px solid var(--white);background:linear-gradient(160deg,#f3f3f3,#d8d8d8)}
.video-frame svg{position:absolute;left:120px;top:62px}
.ad{left:421px;top:49px;width:182px;height:174px;background:linear-gradient(90deg,#1b1b1b 0%,#3a3a3a 60%,#8c8c8c 100%);text-align:center;font-family:'Montserrat',sans-serif}
.ad-holistic{position:absolute;left:0;width:150px;top:23px;font-weight:300;font-size:24px;color:var(--yellow)}
.ad-sub{position:absolute;left:0;width:150px;top:56px;font-weight:600;font-size:8.6px}
.ad-want{position:absolute;left:0;width:160px;top:72px;font-size:6px}
.ad-soon{position:absolute;left:35px;top:90px;width:106px;height:23px;background:var(--black);border-radius:3px;color:var(--yellow);font-weight:700;font-size:11px;line-height:23px}
.ad-program{position:absolute;left:0;width:175px;top:123px;color:var(--yellow);font-size:9.6px}
.ad-date{position:absolute;left:0;width:150px;top:137px;font-weight:700;font-size:9.6px}

.site-footer{left:0;top:1153px;width:704px;height:47px;background:var(--white)}
.footer-links{left:100px;top:12px;font-size:7px;color:var(--ink);display:flex;gap:10px}
.copyright{left:100px;top:29px;font-size:7px;color:var(--ink)}
.social{left:584px;top:11px;width:19px;height:19px;border-radius:50%;background:#2b4a8e}
</style>
</head>
<body>
<header class="abs site-header">
  <div class="abs brand">Silverbrook Gymnastics Academy</div>
  <p class="abs tagline">Success only comes through trying</p>
  <section class="abs hero" role="img" aria-label="Close-up photograph of a gymnast's chalked hand gripping a bar">
    <h1 class="abs hero-title">Wholistic Gymnastics Coaching</h1>
    <div class="abs hero-dots"><span></span><span></span><span></span><span></span></div>
  </section>
</header>

<nav class="abs main-nav">
  <a style="left:116px" href="#">HOME</a>
  <a style="left:164px" href="#">FORMS</a>
  <a style="left:212px" href="#">MORE INFO</a>
  <a style="left:281px" href="#">POLICIES</a>
  <a style="left:345px" href="#">CONTACT INFO</a>
  <div class="abs search">Search
    <svg width="8" height="8" viewBox="0 0 8 8"><circle cx="3" cy="3" r="2.2" fill="none" stroke="#333" stroke-width="1"/><line x1="4.6" y1="4.6" x2="7.5" y2="7.5" stroke="#333" stroke-width="1.4"/></svg>
  </div>
</nav>

<h2 class="abs welcome-title">WELCOME TO SILVERBROOK GYMNASTICS ACADEMY (SGA)</h2>
<p class="abs welcome-text">Gymnastics is for everyone, people of all ages, shapes, sizes and capabilities can participate in and enjoy gymnastics, We offer classes from Kindergym to Adult classes SGA is GymState Affiliated club and our coaches are accredited and qualified with National Gymnastics Council .</p>

<section class="abs about" role="img" aria-label="Night photograph of a harbour bridge over water">
  <h2>ABOUT US</h2>
  <p>SGA is newly established family business whose mission is to provide high quality gymnastics program in a wide variety actrivities to suit all ages, levels and ability. Our vision is to become one of the most successful and holistic gymnastics club in Sydney.</p>
</section>

<section class="abs aims">
  <h2>OUR AIM IS TO PROVIDE</h2>
  <article class="aim-card" style="left:101px">
    <div class="aim-photo" role="img" aria-label="Photograph of a rhythmic gymnast with a ribbon" style="background:linear-gradient(135deg,#dcdcdc,#9a9a9a)"></div>
    <p>A family friendly and supportive environment forall gymnasts to enjoy</p>
  </article>
  <article class="aim-card" style="left:275px">
    <div class="aim-photo" role="img" aria-label="Photograph of a gymnast landing after a vault" style="background:linear-gradient(180deg,#9fb0d6,#3c56a8)"></div>
    <p>High quality, dedicated and motivated coaches</p>
  </article>
  <article class="aim-card" style="left:450px">
    <div class="aim-photo" role="img" aria-label="Photograph of a young gymnast stretching on a blue floor" style="background:linear-gradient(180deg,#3f63a8,#24428a)"></div>
    <p>Progressive and enjoyable recreational and competitive gymnastics programs</p>
  </article>
</section>

<section class="abs media">
  <h3 class="videos-title">FEATURED VIDEOS</h3>
  <svg class="abs video-arrows" width="16" height="10" viewBox="0 0 16 10"><polyline points="5,1 1,5 5,9" fill="none" stroke="#fff" stroke-width="2"/><polyline points="11,1 15,5 11,9" fill="none" stroke="#fff" stroke-width="2"/></svg>
  <h3 class="ads-title">Advertisements</h3>
  <div class="abs video-frame" role="img" aria-label="Video thumbnail of a drawn gymnast on parallel bars">
    <svg width="48" height="48" viewBox="0 0 48 48"><circle cx="24" cy="24" r="21" fill="none" stroke="#444" stroke-width="4"/><polygon points="19,14 34,24 19,34" fill="#444"/></svg>
  </div>
  <div class="abs ad" role="img" aria-label="Advertisement with a photograph of a gymnast on a dark background">
    <div class="ad-holistic">HOLISTIC</div>
    <div class="ad-sub">GYMNASTICS COACHING</div>
    <div class="ad-want">WANT TO JOIN OUR HOLIDAY PROGRAM</div>
    <div class="ad-soon">COMING SOON</div>
    <div class="ad-program">SCHOOL HOLIDAY PROGRAM</div>
    <div class="ad-date">JANUARY 2015</div>
  </div>
</section>

<footer class="abs site-footer">
  <div class="abs footer-links"><span>HOME</span><span>|</span><span>FORMS</span><span>|</span><span>MORE INFO</span><span>|</span><span>POLICIES</span><span>|</span><span>CONTACT INFO</span></div>
  <p class="abs copyright">© 2014 COMPANY NAME , ALL RIGHST RESERVED</p>
  <div class="abs social"></div>
</footer>
</body>
</html>
```